Tavorin - adding eCommerce section to our current website

http://brimfold-works.com/products/

We would like to incorporate an eCommerce section into our current website to have a secure option for customers to purchase products from our site. We would also like to have the option to be able to set up separate accounts and have our customers log in and see all of our products with their own set of prices that are different from the main catalog. It needs to include a platform where we can edit each element/costumer account easily. Our site currently is Processwire. We're also familiar with Wordpress sites and have knowledge of Opencart. We would like your help with an innovative design and a way to incorporate all that we need into a package.

The look and feel should be somewhat similar to the current website but please feel free to propose different looks that have our brand colors.

Target Market(s)

offices, malls, businesses, sports venue

Coding

Coded - Design and coding required

Number of Pages Required

3 page

Font styles to use
Sans Serif

Requirements
Must have
• Shopping cart and payment options, able to add/remove products price/description/etc, create and remove accounts with different set of pricing.
Nice to have
• Quick preview of the products

```html
<!DOCTYPE html>
<html lang="en">
<head>
<meta charset="utf-8">
<title>Tavorin Lighting Solutions – LED Products</title>
<link href="https://fonts.googleapis.com/css2?family=Open+Sans:ital,wght@0,400;0,600;0,700;0,800;1,400&display=swap" rel="stylesheet">
<style>
:root{
  --navy:#0b3d86;
  --navy-dark:#0a3470;
  --sky:#3a8fd4;
  --sky-light:#4aa3e0;
  --text:#555;
  --muted:#888;
  --line:#e6e6e6;
  --panel:#f5f5f5;
  --white:#fff;
  --price:#0b3d86;
  --strike:#bbb;
}
*{box-sizing:border-box;margin:0;padding:0}
html,body{width:730px;height:1200px;overflow:hidden}
body{position:relative;background:var(--white);font-family:"Open Sans",Arial,sans-serif;color:var(--text)}
.abs{position:absolute}

/* header */
.brand{left:60px;top:16px;display:flex;align-items:center;gap:6px}
.brand-mark{width:30px;height:30px;background:var(--navy)}
.brand-name{font-weight:800;font-size:19px;color:var(--navy);line-height:1}
.brand-sub{font-weight:700;font-size:7px;color:var(--navy);letter-spacing:.3px}
.nav{left:278px;top:25px;display:flex;gap:0;font-size:7.5px;color:#555;text-transform:uppercase;letter-spacing:.3px}
.nav span{margin-right:36px}
.nav-icons{left:632px;top:23px;display:flex;gap:12px}

/* hero */
.hero{left:59px;top:64px;width:610px;height:295px;background:radial-gradient(circle at 30% 40%,#7fa9e0 0%,#3d64b8 40%,#243f8a 75%,#3a2f6e 100%)}
.hero-bulb{left:470px;top:110px;width:190px;height:215px;border-radius:40% 40% 30% 30%;background:linear-gradient(135deg,#f5f7fb,#b8c0cc 60%,#8a93a0)}
.hero-kicker{left:97px;top:138px;color:var(--white);font-weight:800;font-size:23px;letter-spacing:.3px}
.hero-title{left:96px;top:164px;color:var(--white);font-weight:800;font-size:44px;letter-spacing:.5px}
.hero-btn{left:97px;top:228px;width:175px;height:30px;border:2px solid var(--white);color:var(--white);font-weight:700;font-size:10.5px;display:flex;align-items:center;justify-content:center}
.hero-dots{left:100px;top:332px;display:flex;gap:3px}
.hero-dots i{width:5px;height:5px;border-radius:50%;background:var(--white)}
.hero-dots i.on{background:var(--navy)}

/* side lists */
.side-head{left:60px;width:138px;height:28px;background:var(--sky);color:var(--white);font-weight:700;font-size:10px;padding:0 10px;display:flex;align-items:center;letter-spacing:.2px}
.side-list{left:60px;width:138px;border:1px solid var(--line);border-top:0}
.side-list li{list-style:none;height:27px;border-bottom:1px solid var(--line);display:flex;align-items:center;padding:0 10px;font-size:8.5px;color:#666}
.side-list li:last-child{border-bottom:0}
.side-list li::before{content:"";width:4px;height:4px;border:1.3px solid var(--navy);border-radius:50%;margin-right:6px}
.side-list li::after{content:"»";margin-left:auto;font-size:9px;color:#777}

.new-list{left:60px;top:712px;width:138px;height:250px;border:1px solid var(--line);border-top:0}
.new-item{position:absolute;left:10px;display:flex;gap:8px}
.new-thumb{width:42px;height:34px;background:linear-gradient(135deg,#f1f4f8,#c9d6e4)}
.new-info{font-size:7.5px;color:#777;line-height:1.4}
.new-info b{display:block;color:var(--price);font-size:8px;font-weight:600}
.new-info s{color:var(--strike);font-size:6.5px}

.newsletter{left:60px;top:978px;width:138px;height:132px;background:var(--sky);padding:12px 10px}
.newsletter h3{color:var(--white);font-size:10px;font-weight:700;margin-bottom:12px}
.field{height:23px;background:var(--white);font-size:7px;color:#666;display:flex;align-items:center;padding:0 6px;margin-bottom:5px}
.submit{margin-top:10px;width:58px;height:22px;background:var(--navy-dark);color:var(--white);font-size:7.5px;font-weight:700;border-radius:3px;display:flex;align-items:center;justify-content:center}

/* featured */
.main-head{left:220px;width:450px;height:27px;background:var(--navy);color:var(--white);font-weight:700;font-size:10px;padding:0 15px;display:flex;align-items:center;justify-content:space-between}
.card{width:141px;height:162px;border:1px solid var(--line);background:var(--white)}
.card-img{height:93px;background:var(--panel);display:flex;align-items:center;justify-content:center}
.card-img div{width:66px;height:60px}
.card-name{text-align:center;font-size:8px;color:#666;margin-top:14px}
.card-price{text-align:center;font-size:9px;font-weight:700;color:var(--price);margin-top:5px}
.card-price s{font-weight:400;font-size:7px;color:var(--strike);margin-left:3px}
.stars{text-align:center;font-size:7px;color:#999;letter-spacing:1px;margin-top:3px}

/* banner */
.why{left:220px;top:781px;width:450px;height:108px;background:linear-gradient(90deg,#1a76bf,#3c9fde 60%,#55b4ea)}
.why h2{position:absolute;left:24px;top:22px;color:var(--white);font-weight:700;font-size:14.5px;line-height:1.55}
.why p{position:absolute;left:24px;top:75px;color:var(--white);font-size:8px}
.why-bulb{left:540px;top:800px;width:125px;height:80px;border-radius:45% 20% 20% 45%;background:linear-gradient(120deg,#ffffff,#dce6ef 70%,#b7c3cf)}

/* testimonials */
.testi{left:220px;top:936px;width:450px;height:174px;border:1px solid var(--line);border-top:0}
.avatar{left:238px;top:963px;width:43px;height:43px;border-radius:50%;background:linear-gradient(160deg,#d7a98a,#7a4a32)}
.quote{left:293px;top:961px;width:362px;font-style:italic;font-size:6.9px;line-height:1.85;color:#777}
.author{left:293px;top:1020px;font-size:8px;color:var(--sky)}
.clients{left:240px;top:1062px;display:flex;gap:34px;align-items:center}
.client{display:flex;align-items:center;gap:6px;color:#8bb5e0;font-weight:800;font-size:15px}
.client i{width:22px;height:22px;background:#8bb5e0}

/* footer */
.footer{left:0;top:1141px;width:730px;height:59px;background:var(--navy-dark)}
.copy{left:62px;top:1165px;color:var(--white);font-size:7.5px}
.social{left:328px;top:1164px;display:flex;gap:12px;color:var(--white);font-size:7.5px;font-weight:600}
.pay{left:535px;top:1163px;display:flex;gap:4px}
.pay i{width:20px;height:13px;border-radius:2px;background:#d9e4f2}
</style>
</head>
<body>

<header>
  <div class="abs brand">
    <div class="brand-mark"></div>
    <div><div class="brand-name">TAVORIN</div><div class="brand-sub">LIGHTING SOLUTIONS</div></div>
  </div>
  <nav class="abs nav"><span>Products</span><span>Galleries</span><span>Advantage</span><span>Vendors</span><span>Contact</span></nav>
  <div class="abs nav-icons">
    <svg width="10" height="10" viewBox="0 0 10 10"><circle cx="4" cy="4" r="3" fill="none" stroke="#777" stroke-width="1.5"/><line x1="6.2" y1="6.2" x2="9.3" y2="9.3" stroke="#777" stroke-width="1.6"/></svg>
    <svg width="11" height="10" viewBox="0 0 11 10"><path d="M0 1h2l1.5 5h6l1-4H3" fill="none" stroke="#777" stroke-width="1.3"/><circle cx="4.5" cy="8.5" r="1" fill="#777"/><circle cx="8.5" cy="8.5" r="1" fill="#777"/></svg>
  </div>
</header>

<section class="abs hero" role="img" aria-label="Blurred blue bokeh lights background"></section>
<div class="abs hero-bulb" role="img" aria-label="Photo of two LED bulbs"></div>
<div class="abs hero-kicker">EVERYTHING YOU NEED</div>
<div class="abs hero-title">LED PRODUCTS</div>
<div class="abs hero-btn">REQUEST CUSTOM SOLUTION »</div>
<div class="abs hero-dots"><i></i><i></i><i class="on"></i><i></i></div>

<aside>
  <div class="abs side-head" style="top:381px">INTERIOR PRODUCTS</div>
  <ul class="abs side-list" style="top:409px"><li>Grid Ceiling Troffers</li><li>Warehouse</li><li>Open Ceiling</li><li>Downlights</li></ul>
  <div class="abs side-head" style="top:531px">EXTERIOR PRODUCTS</div>
  <ul class="abs side-list" style="top:559px"><li>Parking Lot</li><li>Wall Packs</li><li>Parking Garage</li><li>Canopy</li></ul>
  <div class="abs side-head" style="top:684px">NEW PRODUCTS</div>
  <div class="abs new-list">
    <div class="new-item" style="top:8px"><div class="new-thumb" role="img" aria-label="Panel light product photo"></div><div class="new-info">Parking Lot prouct<b>$ 340.00</b><s>$ 500.00</s></div></div>
    <div class="new-item" style="top:56px"><div class="new-thumb" role="img" aria-label="Square fixture product photo"></div><div class="new-info">Parking Lot prouct<b>$ 340.00</b><s>$ 500.00</s></div></div>
    <div class="new-item" style="top:105px"><div class="new-thumb" role="img" aria-label="Grid fixture product photo"></div><div class="new-info">Parking Lot prouct<b>$ 340.00</b><s>$ 500.00</s></div></div>
    <div class="new-item" style="top:153px"><div class="new-thumb" role="img" aria-label="Linear fixture product photo"></div><div class="new-info">Parking Lot prouct<b>$ 340.00</b><s>$ 500.00</s></div></div>
    <div class="new-item" style="top:201px"><div class="new-thumb" role="img" aria-label="Troffer product photo"></div><div class="new-info">Parking Lot prouct<b>$ 340.00</b><s>$ 500.00</s></div></div>
  </div>
  <form class="abs newsletter">
    <h3>NEWSLETTER</h3>
    <div class="field">Name:</div>
    <div class="field">Email:</div>
    <div class="submit">SUBMIT</div>
  </form>
</aside>

<main>
  <div class="abs main-head" style="top:381px"><span>FEATURED PRODUCTS</span>
    <svg width="10" height="8" viewBox="0 0 10 8"><path d="M3 1L0.8 4L3 7M7 1L9.2 4L7 7" fill="none" stroke="#fff" stroke-width="1.2"/></svg></div>

  <div class="abs card" style="left:220px;top:418px"><div class="card-img"><div role="img" aria-label="Round recessed down light" style="border-radius:50%;background:radial-gradient(#fff,#d8d8d8)"></div></div><div class="card-name">6" Recessed Down Light</div><div class="card-price">$ 340.00<s>$ 500.00</s></div><div class="stars">☆☆☆☆☆</div></div>
  <div class="abs card" style="left:374px;top:418px"><div class="card-img"><div role="img" aria-label="Linear tube fixture" style="background:linear-gradient(135deg,#f4f4f4,#c9c9c9)"></div></div><div class="card-name">6" Recessed Down Light</div><div class="card-price">$ 340.00<s>$ 500.00</s></div><div class="stars">☆☆☆☆☆</div></div>
  <div class="abs card" style="left:529px;top:418px"><div class="card-img"><div role="img" aria-label="Street area light" style="background:linear-gradient(135deg,#3a4560,#0f1420)"></div></div><div class="card-name">6" Recessed Down Light</div><div class="card-price">$ 340.00<s>$ 500.00</s></div><div class="stars">☆☆☆☆☆</div></div>
  <div class="abs card" style="left:220px;top:595px"><div class="card-img"><div role="img" aria-label="Wall pack fixture" style="background:linear-gradient(135deg,#9a9a9a,#505050)"></div></div><div class="card-name">6" Recessed Down Light</div><div class="card-price">$ 340.00<s>$ 500.00</s></div><div class="stars">☆☆☆☆☆</div></div>
  <div class="abs card" style="left:374px;top:595px"><div class="card-img"><div role="img" aria-label="Canopy fixture" style="background:linear-gradient(135deg,#2a2a2a,#0a0a0a)"></div></div><div class="card-name">6" Recessed Down Light</div><div class="card-price">$ 340.00<s>$ 500.00</s></div><div class="stars">☆☆☆☆☆</div></div>
  <div class="abs card" style="left:529px;top:595px"><div class="card-img"><div role="img" aria-label="Garage fixture" style="background:linear-gradient(135deg,#2a2a2a,#0a0a0a)"></div></div><div class="card-name">6" Recessed Down Light</div><div class="card-price">$ 340.00<s>$ 500.00</s></div><div class="stars">☆☆☆☆☆</div></div>

  <section class="abs why">
    <h2>Why select Tavorin Lighting Solutions<br>over traditional lighting providers?</h2>
    <p>Our Core Technologies • Resource Center</p>
  </section>
  <div class="abs why-bulb" role="img" aria-label="Photo of an LED bulb"></div>

  <div class="abs main-head" style="top:909px"><span>OUR CLIENTS &amp; TESTIMONIALS</span></div>
  <div class="abs testi"></div>
  <div class="abs avatar" role="img" aria-label="Client portrait photo"></div>
  <p class="abs quote">I send Tavorin Lighting Solutions my floor plan and they design my lighting system according to the specifica-tion I have set. Having a design engineer construct your lighting system ensures proper lighting levels with the minimum fixtures and saves money both in construction and energy cost. Also having a trusted lighting supplier that caters to Crestwood Pizza Franchisee's helps to keep construction cost in line"</p>
  <div class="abs author">Marcus Hale, Crestwood Franchisee, Owner at Harbor Pie Company</div>
  <div class="abs clients">
    <div class="client"><i></i>KELVORA</div>
    <div class="client"><i></i>ORRIN</div>
    <div class="client"><i></i>TAVORIN</div>
  </div>
</main>

<footer>
  <div class="abs footer"></div>
  <div class="abs copy">© 2015 Tavorin Lighting Solutions. All Rights Reserved.</div>
  <div class="abs social"><span>Pixlo</span><span>Loopa</span><span>Vidora</span><span>Facet</span><span>Chirply</span></div>
  <div class="abs pay"><i></i><i></i><i></i><i></i><i></i><i></i></div>
</footer>

</body>
</html>
```